Corvalen Capital Modern Business Card

We need a modern business card template designed for Corvalen Capital.
Corvalen Capital is a diversified global cryptocurrency investment fund.

The font under the logo: Hiragino Kaku Gothic Pro

Color Hexcode: Main colors white (ffffff) & teal (188383), we are open to adding #fcca46 as an accent

Need time to get feedback from my team and to make sure designers better understand the brief.

Target Market(s)

Accredited Investors, high net worth individuals and institutional investors

Industry/Entity Type

Investment

Contact Information for Business Card

Contact Information should contain
Name
main phone +1 720 555 0147
cell
email

Font styles to use
Sans Serif
Other font styles liked:
• Hiragino Kaku Gothic Pro

Requirements
Must have
• would like to have icons that identify the contact information
• include our website: www.corvalencapital.example
• include our Tagline: Diversified Crypto Investment Funds
Nice to have
• Would like to have a simple back side with the logo (without the words) and plenty of space

```html
<!DOCTYPE html>
<html lang="en">
<head>
<meta charset="utf-8">
<title>Corvalen Capital — Business Card</title>
<link href="https://fonts.googleapis.com/css2?family=Noto+Sans+JP:wght@400;500;700&display=swap" rel="stylesheet">
<style>
  :root {
    --backdrop: #3a3a3a;
    --card: #232323;
    --teal: #188383;
    --teal-bright: #1a9696;
    --white: #ffffff;
    --accent: #fcca46;
  }
  * { margin: 0; padding: 0; box-sizing: border-box; }
  html, body { width: 799px; height: 1200px; overflow: hidden; }
  body {
    background: var(--backdrop);
    font-family: "Noto Sans JP", "Hiragino Kaku Gothic Pro", sans-serif;
    position: relative;
  }
  .card {
    position: absolute;
    left: 90px;
    width: 620px;
    height: 354px;
    background: var(--card);
    border-radius: 22px;
    overflow: hidden;
    box-shadow: 0 10px 28px rgba(0,0,0,.45);
  }
  .card--front { top: 130px; }
  .card--back { top: 700px; }

  .wordmark {
    display: flex;
    align-items: center;
    gap: 12px;
    font-weight: 400;
    letter-spacing: 1px;
    text-transform: uppercase;
    white-space: nowrap;
  }
  .wordmark__square { width: 14px; height: 14px; background: currentColor; flex: none; }

  .card--front .wordmark {
    position: absolute;
    left: 0; right: 0; top: 150px;
    justify-content: center;
    color: var(--teal-bright);
    font-size: 34px;
  }

  .card--back .wordmark {
    position: absolute;
    left: 36px; top: 118px;
    color: var(--white);
    font-size: 24px;
  }

  .contact { position: absolute; left: 340px; top: 76px; color: var(--white); }
  .contact__name { color: var(--teal-bright); font-weight: 700; font-size: 26px; line-height: 1.1; }
  .contact__title { font-size: 15px; margin-top: 2px; margin-bottom: 16px; }
  .contact__list { list-style: none; }
  .contact__item { display: flex; align-items: center; gap: 10px; font-size: 14.5px; line-height: 22px; white-space: nowrap; }
  .contact__icon { width: 14px; height: 14px; flex: none; fill: var(--teal-bright); }

  .band {
    position: absolute;
    left: 0; right: 0; bottom: 0;
    height: 70px;
    background: var(--teal-bright);
    border-top: 2px solid var(--accent);
    display: flex;
    align-items: center;
    padding-left: 120px;
  }
  .band__tagline { color: var(--white); font-size: 17px; white-space: nowrap; }
</style>
</head>
<body>

<section class="card card--front" aria-label="Card front">
  <div class="wordmark"><span class="wordmark__square"></span>Corvalen Capital</div>
</section>

<section class="card card--back" aria-label="Card back">
  <div class="wordmark"><span class="wordmark__square"></span>Corvalen Capital</div>

  <div class="contact">
    <div class="contact__name">Marcus Elden</div>
    <div class="contact__title">Portfolio Engineer</div>
    <ul class="contact__list">
      <li class="contact__item">
        <svg class="contact__icon" viewBox="0 0 16 16"><path d="M3 1h3l1.5 4-2 1.2a9 9 0 0 0 4.3 4.3L11 8.5l4 1.5v3a2 2 0 0 1-2 2C7 15 1 9 1 3a2 2 0 0 1 2-2z"/></svg>
        +1 720 555 0147
      </li>
      <li class="contact__item">
        <svg class="contact__icon" viewBox="0 0 16 16"><path d="M4.5 0h7A1.5 1.5 0 0 1 13 1.5v13a1.5 1.5 0 0 1-1.5 1.5h-7A1.5 1.5 0 0 1 3 14.5v-13A1.5 1.5 0 0 1 4.5 0zM5 2v10h6V2zm3 11a1 1 0 1 0 0 2 1 1 0 0 0 0-2z"/></svg>
        +1 303 555 0192
      </li>
      <li class="contact__item">
        <svg class="contact__icon" viewBox="0 0 16 16"><path d="M0 3h16v10H0zm1.5 1.2V12h13V4.2L8 9z"/></svg>
        marcus@corvalencapital.example
      </li>
      <li class="contact__item">
        <svg class="contact__icon" viewBox="0 0 16 16"><path d="M8 0a8 8 0 1 0 0 16A8 8 0 0 0 8 0zm5.9 7h-2.6a12 12 0 0 0-1-4.7A6 6 0 0 1 13.9 7zM8 2c.8 1 1.3 2.8 1.4 5H6.6C6.7 4.8 7.2 3 8 2zM5.7 2.3a12 12 0 0 0-1 4.7H2.1a6 6 0 0 1 3.6-4.7zM2.1 9h2.6a12 12 0 0 0 1 4.7A6 6 0 0 1 2.1 9zM8 14c-.8-1-1.3-2.8-1.4-5h2.8c-.1 2.2-.6 4-1.4 5zm2.3-.3a12 12 0 0 0 1-4.7h2.6a6 6 0 0 1-3.6 4.7z"/></svg>
        www.corvalencapital.example
      </li>
    </ul>
  </div>

  <div class="band">
    <span class="band__tagline">Diversified Crypto Investment Funds</span>
  </div>
</section>

</body>
</html>
```